New Managed IT company needs a business card

We are an IT management and support company that needs a business card design. I have a logo that I'll provide. Blues and blacks match the logo, but i'm open to anything. I want the card to help people take us seriously, but still have some energy and fun in it. The card should communicate stability and a solid company.

Target Market(s)

Target market includes Owners and Presidents at small businesses of 20 - 100 employees in the Pittsburgh PA area.

Industry/Entity Type

Information Technology

Contact Information for Business Card

i am open to other designs, but i imagine having only the logo on one side and then the logo plus all contact details on the other side.

Requirements
Must have
• Our logo
• Company name is optional if the logo makes it obvious
• A name - Lew Tasker
• A title - President
• A phone number - 724-XXX-XXXX
• A mobile phone number - 724-516-0471
• An email address - ltasker@brightlanetech.com
• a website - brightlanetech.com or www.brightlanetech.com
Nice to have
• some people tell me the logo feels like a superhero theme, some fun with that idea might be good. I'm open to ideas.
Should not have
• stock photos of people or computers - especially old looking stuff.

```html
<!DOCTYPE html>
<html lang="en">
<head>
<meta charset="utf-8">
<title>Brightlane Tech — Business Card</title>
<link rel="stylesheet" href="https://fonts.googleapis.com/css2?family=Open+Sans:wght@400;600;700&display=swap">
<style>
  :root {
    --brand-blue: #0a62b4;
    --brand-blue-light: #7aaed8;
    --accent-blue: #1592d8;
    --ink: #1a1a1a;
    --band-black: #171717;
    --paper: #ffffff;
    --backdrop: #e9e6e1;
  }
  * { box-sizing: border-box; margin: 0; padding: 0; }
  html, body {
    width: 1200px; height: 900px; overflow: hidden;
    background: var(--backdrop);
    font-family: "Open Sans", Arial, sans-serif;
  }
  .canvas { position: relative; width: 1200px; height: 900px; }

  .card {
    position: absolute; width: 540px; height: 310px;
    box-shadow: 0 10px 28px rgba(0,0,0,.18);
    overflow: hidden;
  }

  /* Back of card */
  .card-back {
    left: 70px; top: 140px;
    background: var(--brand-blue);
    display: flex; align-items: center; justify-content: center; gap: 18px;
  }
  .card-back .mark-dot {
    width: 64px; height: 64px; border-radius: 50%;
    background: var(--brand-blue-light);
  }
  .card-back .wordmark {
    color: var(--brand-blue-light);
    font-weight: 700; font-size: 38px; letter-spacing: 1px;
  }

  /* Front of card */
  .card-front { left: 590px; top: 450px; background: var(--paper); }
  .card-front .bands { position: absolute; inset: 0; }

  .holder { position: absolute; left: 34px; top: 44px; }
  .holder-name { color: var(--accent-blue); font-weight: 700; font-size: 18px; }
  .holder-title { color: var(--ink); font-size: 14px; margin-top: 4px; margin-left: 8px; }

  .brand {
    position: absolute; right: 36px; top: 62px;
    display: flex; align-items: center; gap: 10px;
  }
  .brand .mark-dot { width: 40px; height: 40px; border-radius: 50%; background: var(--ink); }
  .brand .wordmark { color: var(--ink); font-weight: 700; font-size: 26px; letter-spacing: 1px; }

  .contacts {
    position: absolute; left: 74px; top: 160px;
    list-style: none; color: var(--ink); font-size: 14px; line-height: 22px;
  }
  .contacts li { display: flex; align-items: center; gap: 8px; }
  .contacts svg { width: 12px; height: 12px; fill: var(--ink); }

  .website {
    position: absolute; left: 60px; top: 259px;
    color: var(--paper); font-size: 15px; letter-spacing: .3px;
  }
</style>
</head>
<body>
<main class="canvas">

  <section class="card card-back" aria-label="Card back">
    <span class="mark-dot"></span>
    <span class="wordmark">BRIGHTLANE TECH</span>
  </section>

  <section class="card card-front" aria-label="Card front">
    <svg class="bands" viewBox="0 0 540 310" width="540" height="310" aria-hidden="true">
      <path d="M0 172 H36 Q58 205 52 246 H0 Z" fill="var(--accent-blue)"/>
      <path d="M356 222 L378 202 H540 V222 Z" fill="var(--accent-blue)"/>
      <path d="M0 246 H330 L356 222 H540 V294 H0 Z" fill="var(--band-black)"/>
      <circle cx="500" cy="222" r="15" fill="var(--band-black)"/>
    </svg>

    <div class="holder">
      <p class="holder-name">Lew Tasker</p>
      <p class="holder-title">President</p>
    </div>

    <div class="brand">
      <span class="mark-dot"></span>
      <span class="wordmark">BRIGHTLANE TECH</span>
    </div>

    <ul class="contacts">
      <li><svg viewBox="0 0 12 12"><path d="M1 4 Q6 0 11 4 L9 6 L7 5 V4 H5 V5 L3 6 Z M2 7 H10 V11 H2 Z"/></svg>724-XXX-XXXX</li>
      <li><svg viewBox="0 0 12 12"><path d="M3 0 H9 V12 H3 Z M4 1.5 V9.5 H8 V1.5 Z" fill-rule="evenodd"/></svg>724-516-0471</li>
      <li><svg viewBox="0 0 12 12"><path d="M0 2 H12 V10 H0 Z M1 3 L6 7 L11 3 Z" fill-rule="evenodd"/></svg>ltasker@brightlanetech.com</li>
    </ul>

    <p class="website">www.brightlanetech.com</p>
  </section>

</main>
</body>
</html>
```